Brightpath Strategic Advisers F.Z.E
Professional
Khalid Yousef Nasser
Founder & CEO
Corvana Trade Park
info@bsa-qx.com
www.bsa-qx.com
Training & Consultancy on:
QBXR Assessment & Training
Leadership Development & Coaching
Change Management
Strategy Management
Performance Management
Quality & Process Management
TQM
HR Development
HR Procedures & Regulation
Logo & Full Stationeries & P.P Presentation first page and continues sheet & Proposal document cover & continues sheet

```html
<!DOCTYPE html>
<html lang="en">
<head>
<meta charset="utf-8">
<title>Brightpath Strategic Advisers F.Z.E – Business Cards</title>
<link rel="stylesheet" href="https://fonts.googleapis.com/css2?family=Arimo:ital,wght@0,400;0,700;1,400&family=Cinzel:wght@400&display=swap">
<style>
  :root {
    --stage: #ece7df;
    --card-light: #ffffff;
    --card-dark: #1c1b1a;
    --orange: #f28a1c;
    --orange-deep: #e0630d;
    --amber: #ffb23a;
    --grey: #6b6b6b;
    --grey-light: #c9c9c9;
    --ink-dark: #3a3a3a;
    --ink-light: #f1f1f1;
    --caption: #3b3733;
  }
  * { box-sizing: border-box; margin: 0; padding: 0; }
  html, body {
    width: 1200px; height: 794px; overflow: hidden;
    background: var(--stage);
    font-family: "Arimo", Arial, sans-serif;
  }
  .sheet { position: relative; width: 1200px; height: 794px; }

  .card {
    position: absolute; width: 547px; height: 324px; overflow: hidden;
    box-shadow: 0 3px 10px rgba(0,0,0,.25);
  }
  .card--light { background: var(--card-light); color: var(--ink-dark); }
  .card--dark { background: var(--card-dark); color: var(--ink-light); }
  .card--front-a { left: 31px; top: 12px; }
  .card--front-b { left: 619px; top: 12px; }
  .card--back-a { left: 31px; top: 403px; }
  .card--back-b { left: 619px; top: 403px; }

  .card__swoosh { position: absolute; inset: 0; width: 100%; height: 100%; }

  .contact { position: absolute; left: 358px; top: 20px; font-size: 11px; line-height: 17px; }
  .contact__place { font-style: italic; margin-bottom: 5px; }
  .contact__row { display: flex; }
  .contact__label { width: 42px; color: var(--orange); font-weight: 700; }

  .brand {
    position: absolute; left: 28px; top: 160px; width: 300px;
    display: flex; align-items: center; gap: 10px;
  }
  .brand__dot { width: 18px; height: 18px; border-radius: 50%; background: var(--orange); flex: none; }
  .brand__name {
    font-size: 19px; font-weight: 700; line-height: 22px; text-transform: uppercase;
    color: #4a4a4a;
  }
  .card--dark .brand__name { color: var(--ink-light); }

  .holder { position: absolute; left: 325px; top: 268px; font-size: 11px; line-height: 15px; }
  .holder__name { color: var(--amber); }
  .holder__role { color: #ffffff; }

  .services { position: absolute; left: 262px; top: 95px; font-size: 10.5px; line-height: 20px; }
  .services__title { color: var(--orange); font-weight: 700; font-size: 12px; margin-bottom: 6px; }
  .services__list { list-style: none; }

  .accent-circle {
    position: absolute; left: 160px; top: 48px; width: 44px; height: 44px; border-radius: 50%;
    background: var(--grey-light); opacity: .7;
  }
  .card--dark .accent-circle { background: #6d6d6d; }

  .caption {
    position: absolute; width: 547px; text-align: center;
    font-family: "Cinzel", Georgia, serif; font-size: 21px; letter-spacing: 2px; color: var(--caption);
  }
  .caption--front-a { left: 31px; top: 346px; }
  .caption--front-b { left: 619px; top: 346px; }
  .caption--back-a { left: 31px; top: 750px; }
  .caption--back-b { left: 619px; top: 750px; }
</style>
</head>
<body>
<main class="sheet">

  <!-- Front, light -->
  <section class="card card--light card--front-a">
    <svg class="card__swoosh" viewBox="0 0 547 324" aria-hidden="true">
      <defs>
        <linearGradient id="bandLight" x1="0" y1="0" x2="1" y2="0">
          <stop offset="0" stop-color="#ffc27a"/>
          <stop offset=".5" stop-color="#f28a1c"/>
          <stop offset="1" stop-color="#e0630d"/>
        </linearGradient>
      </defs>
      <path d="M0 324 L0 300 C160 250 330 215 547 110 L547 324 Z" fill="url(#bandLight)"/>
      <path d="M0 270 C170 225 340 190 547 95" fill="none" stroke="#8e8e8e" stroke-width="5"/>
      <path d="M300 14 C420 20 500 40 547 60" fill="none" stroke="#f28a1c" stroke-width="3"/>
      <path d="M0 292 C170 245 340 210 547 112" fill="none" stroke="#ffffff" stroke-width="3"/>
    </svg>
    <div class="contact">
      <p class="contact__place">Corvana Trade Park</p>
      <p class="contact__row"><span class="contact__label">Phone</span>00971 555018274</p>
      <p class="contact__row"><span class="contact__label">Email</span>info@bsa-qx.com</p>
      <p class="contact__row"><span class="contact__label">Web</span>www.bsa-qx.com</p>
    </div>
    <div class="brand"><span class="brand__dot"></span><p class="brand__name">Brightpath Strategic Advisers F.Z.E</p></div>
    <div class="holder">
      <p class="holder__name">Khalid Yousef Nasser</p>
      <p class="holder__role">Founder &amp; CEO</p>
    </div>
  </section>
  <p class="caption caption--front-a">Business Card Front A</p>

  <!-- Front, dark -->
  <section class="card card--dark card--front-b">
    <svg class="card__swoosh" viewBox="0 0 547 324" aria-hidden="true">
      <defs>
        <linearGradient id="bandDark" x1="0" y1="0" x2="1" y2="0">
          <stop offset="0" stop-color="#ffc27a"/>
          <stop offset=".5" stop-color="#f28a1c"/>
          <stop offset="1" stop-color="#e0630d"/>
        </linearGradient>
      </defs>
      <path d="M0 324 L0 300 C160 250 330 215 547 110 L547 324 Z" fill="url(#bandDark)"/>
      <path d="M0 270 C170 225 340 190 547 95" fill="none" stroke="#9a9a9a" stroke-width="5"/>
      <path d="M300 14 C420 20 500 40 547 60" fill="none" stroke="#f28a1c" stroke-width="3"/>
      <path d="M0 292 C170 245 340 210 547 112" fill="none" stroke="#1c1b1a" stroke-width="3"/>
    </svg>
    <div class="contact">
      <p class="contact__place">Corvana Trade Park</p>
      <p class="contact__row"><span class="contact__label">Phone</span>00971 555018274</p>
      <p class="contact__row"><span class="contact__label">Email</span>info@bsa-qx.com</p>
      <p class="contact__row"><span class="contact__label">Web</span>www.bsa-qx.com</p>
    </div>
    <div class="brand"><span class="brand__dot"></span><p class="brand__name">Brightpath Strategic Advisers F.Z.E</p></div>
    <div class="holder">
      <p class="holder__name">Khalid Yousef Nasser</p>
      <p class="holder__role">Founder &amp; CEO</p>
    </div>
  </section>
  <p class="caption caption--front-b">Business Card Front B</p>

  <!-- Back, light -->
  <section class="card card--light card--back-a">
    <span class="accent-circle"></span>
    <div class="services">
      <p class="services__title">Training &amp; Consultancy on:</p>
      <ul class="services__list">
        <li>QBXR Assessment &amp; Training</li>
        <li>Leadership Development &amp; Coaching</li>
        <li>Change Management</li>
        <li>Strategy Management</li>
        <li>Performance Management</li>
        <li>Quality &amp; Process Management</li>
        <li>TQM</li>
        <li>HR Development</li>
        <li>HR Procedures &amp; Regulation</li>
      </ul>
    </div>
  </section>
  <p class="caption caption--back-a">Business Card Back A</p>

  <!-- Back, dark -->
  <section class="card card--dark card--back-b">
    <span class="accent-circle"></span>
    <div class="services">
      <p class="services__title">Training &amp; Consultancy on:</p>
      <ul class="services__list">
        <li>QBXR Assessment &amp; Training</li>
        <li>Leadership Development &amp; Coaching</li>
        <li>Change Management</li>
        <li>Strategy Management</li>
        <li>Performance Management</li>
        <li>Quality &amp; Process Management</li>
        <li>TQM</li>
        <li>HR Development</li>
        <li>HR Procedures &amp; Regulation</li>
      </ul>
    </div>
  </section>
  <p class="caption caption--back-b">Business Card Back B</p>

</main>
</body>
</html>
```